Medtech Advisory- TLN Ferrow Partners Website

We need a company website, programmed in Typo3.
The design should be clean, modern and simple based on the color and style of our logo.
TLN Ferrow Partners is a Swiss company which assists international medtech companies in relocating all or part of their business to Switzerland.
The site should consist of the following pages: Home, Offering, Customers, Team, Contact us (see also attached pdf file).
Target Market(s)
Medtech Start-ups
Industry/Entity Type
It Company
Coding
Coded - Design and coding required
Requirements
Must have
- Use of the logo provided
- page structure as described above
- programmed in Typo3 so that we can edit ourselves
- responsive for use with mobile devices
Nice to have
- eye catcher to attract readers interest, e.g. visuals

```html
<!DOCTYPE html>
<html lang="en">
<head>
<meta charset="utf-8">
<title>TLN Ferrow Partners – Medtech Advisory</title>
<link rel="stylesheet" href="https://fonts.googleapis.com/css2?family=Lato:wght@400;700;900&display=swap">
<style>
:root{
  --blue:#4f7db3;
  --blue-band:#5a85b6;
  --blue-dark:#3d6698;
  --ink:#1f2430;
  --text:#4a4f58;
  --light:#eef2f7;
  --line:#cfd8e3;
  --footer:#2e353e;
  --white:#ffffff;
}
*{margin:0;padding:0;box-sizing:border-box}
html,body{width:1200px;height:3629px;overflow:hidden}
body{font-family:"Lato",Arial,sans-serif;color:var(--text);background:var(--white);position:relative}
section,header,footer{position:relative;width:1200px}
.abs{position:absolute}
.sec-title{position:absolute;left:0;width:1200px;text-align:center;font-weight:900;font-size:29px;color:var(--ink);letter-spacing:.5px}
.sec-title span{color:var(--blue)}
.sec-rule{position:absolute;left:450px;width:300px;height:2px;background:var(--line)}

/* header */
.site-header{height:106px;background:var(--white)}
.brand{left:99px;top:26px;display:flex;align-items:center;gap:12px;font-size:27px;font-weight:700;color:var(--blue)}
.brand i{display:block;width:30px;height:30px;border-radius:50%;background:var(--blue)}
.phone{left:915px;top:14px;display:flex;align-items:center;gap:12px;font-size:22px;color:var(--ink)}
.phone b{width:32px;height:32px;border-radius:50%;border:2px solid var(--text);display:flex;align-items:center;justify-content:center}
.main-nav{left:351px;top:62px;display:flex;gap:0;font-size:14px;font-weight:700;color:var(--ink);letter-spacing:.4px}
.main-nav a{display:block;padding:8px 16px;border-left:1px solid var(--line);text-decoration:none;color:inherit}
.main-nav a:first-child{border:2px solid var(--blue);color:var(--blue);padding:6px 26px}
.main-nav a:nth-child(2){border-left:none}

/* hero */
.hero{height:506px;background:linear-gradient(180deg,#3f6a6c 0%,#2f5560 40%,#243c55 62%,#3b4f72 78%,#5670a0 100%)}
.hero-title{top:196px;left:0;width:1200px;text-align:center;color:var(--white);font-size:38px;font-weight:700;line-height:54px;text-shadow:0 2px 6px rgba(0,0,0,.6)}
.hero-arrow{top:244px;width:22px;height:22px;border-top:3px solid rgba(255,255,255,.7);border-left:3px solid rgba(255,255,255,.7)}

/* welcome */
.welcome{height:336px}
.welcome-text{left:126px;top:145px;width:948px;text-align:center;font-size:15px;line-height:29px;color:var(--text)}
.btn-outline{left:515px;top:245px;width:170px;height:36px;border:2px solid #b9c7d8;color:var(--blue);font-size:15px;display:flex;align-items:center;justify-content:center;letter-spacing:.5px}

/* what we do */
.what-we-do{height:496px;background:var(--light)}
.wwd-item{width:200px;font-size:13.5px;line-height:17px;color:var(--ink)}
.wwd-item.left{text-align:right}
.wwd-icon{width:54px;height:54px;border-radius:50%;background:var(--white);border:2px solid #9aa7b7;display:flex;align-items:center;justify-content:center}
.hub{left:455px;top:95px;width:290px;height:290px;border-radius:50%;border:16px solid var(--blue);background:var(--white);display:flex;align-items:center;justify-content:center}
.hub-inner{width:232px;height:232px;border-radius:50%;border:3px solid #b9c7d8;display:flex;align-items:center;justify-content:center;text-align:center;font-size:24px;font-weight:700;color:var(--blue);line-height:30px}

/* services */
.services{height:460px;background:linear-gradient(180deg,var(--white) 0,var(--white) 250px,var(--blue-band) 250px)}
.service{top:53px;width:315px}
.service-img{width:315px;height:245px;border:6px solid var(--white);box-shadow:0 3px 10px rgba(0,0,0,.35);position:relative}
.service-badge{position:absolute;left:125px;bottom:-6px;width:64px;height:38px;border-radius:32px 32px 0 0;background:var(--blue);display:flex;justify-content:center;padding-top:8px}
.service h3{margin-top:32px;text-align:center;color:var(--white);font-size:26px;font-weight:700;letter-spacing:.3px}
.btn-pill{margin:22px auto 0;width:130px;height:32px;border-radius:16px;background:var(--white);color:var(--blue-dark);font-size:13px;font-weight:700;display:flex;align-items:center;justify-content:center;gap:10px;box-shadow:0 2px 4px rgba(0,0,0,.3)}
.btn-pill b{width:20px;height:20px;border-radius:50%;background:var(--blue-dark);color:var(--white);font-size:12px;display:flex;align-items:center;justify-content:center}

/* why switzerland */
.why{height:547px;background:var(--light)}
.why-label{width:220px;text-align:center;font-size:18px;line-height:22px;color:var(--ink)}
.dot-arrow{width:22px;height:22px;border-radius:50%;background:#6d93c2;color:var(--white);font-size:12px;display:flex;align-items:center;justify-content:center}

/* team */
.team{height:578px;background:var(--blue-band)}
.team .sec-title{color:var(--white)}
.team-intro{left:300px;top:143px;width:600px;text-align:center;color:var(--white);font-size:14.5px;line-height:26px}
.member{top:213px;width:220px;height:307px;background:var(--white);box-shadow:0 3px 10px rgba(0,0,0,.3);padding:6px}
.member-photo{height:137px;background:linear-gradient(180deg,#d9d9d9,#8c8c8c)}
.member h4{margin-top:18px;text-align:center;font-size:14px;font-weight:900;color:var(--ink);letter-spacing:.4px}
.member p{margin-top:10px;text-align:center;font-size:12.5px;line-height:17px;color:var(--text);padding:0 8px}
.member-plus{position:absolute;left:90px;bottom:-2px;width:40px;height:24px;border-radius:20px 20px 0 0;background:var(--blue);color:var(--white);font-size:20px;font-weight:700;text-align:center;line-height:26px}
.slide-arrow{width:34px;height:44px;background:#9aa3ad;color:var(--white);display:flex;align-items:center;justify-content:center;font-size:18px}

/* subsidiaries */
.subs{height:278px;background:var(--white)}
.sub-logo{top:160px;width:147px;height:63px;border:1px solid #d8dde4;background:var(--white);display:flex;align-items:center;justify-content:center;gap:8px;font-size:18px;font-weight:700;color:#2a2f36}
.sub-logo i{width:16px;height:16px;border-radius:50%;background:#2a2f36}
.thin-arrow{top:180px;width:20px;height:20px;border-top:2px solid #b3bac3;border-left:2px solid #b3bac3}

/* footer */
.site-footer{height:281px;background:var(--footer);color:#d5dae0}
.foot-title{font-size:19px;font-weight:700;color:var(--white)}
.foot-title span{color:#7fa4d3}
.quick-links{list-style:none;font-size:12.5px;line-height:25.5px}
.quick-links li::before{content:"•";margin-right:10px;color:#9aa3ad}
.contact-list{font-size:12.5px;line-height:19px}
.contact-line{display:flex;align-items:center;gap:10px;margin-top:9px;font-size:12.5px}
.contact-line i{width:12px;height:12px;border-radius:50%;background:#7fa4d3;display:block}
.field{width:256px;height:31px;background:var(--white);margin-bottom:13px;font-size:12px;color:#888;padding:8px 10px}
.btn-submit{width:121px;height:31px;background:var(--blue);color:var(--white);font-size:14px;font-weight:700;display:flex;align-items:center;justify-content:center}
.social{display:flex;align-items:center;gap:14px;font-size:12.5px;margin-bottom:17px}
.social i{width:26px;height:26px;border-radius:50%;background:var(--blue);display:block}
.copyright{height:41px;background:var(--blue);color:var(--white);font-size:12.5px;display:flex;align-items:center;justify-content:center}
</style>
</head>
<body>

<header class="site-header">
  <div class="brand abs"><i></i>TLN Ferrow Partners</div>
  <div class="phone abs"><b><svg width="16" height="16" viewBox="0 0 24 24"><path d="M6 2l4 4-2 3c1 3 4 6 7 7l3-2 4 4-3 4C10 22 2 14 2 5z" fill="#4a4f58"/></svg></b>+123 456 7890</div>
  <nav class="main-nav abs">
    <a>HOME</a><a>SERVICES</a><a>WHO WE ADRESS</a><a>OFFERING</a><a>CUSTOMERS</a><a>TEAM</a><a>CONTACT US</a>
  </nav>
</header>

<section class="hero" role="img" aria-label="Evening photograph of a Swiss old town riverside with a church tower and lamp-lit bridge railing">
  <h1 class="hero-title abs">We Assist promising MedTech Companies<br>Interested in Relocating to Switzerland</h1>
  <div class="hero-arrow abs" style="left:58px;transform:rotate(-45deg)"></div>
  <div class="hero-arrow abs" style="left:1122px;transform:rotate(135deg)"></div>
</section>

<section class="welcome">
  <h2 class="sec-title" style="top:50px;font-size:37px;font-weight:700">Welcome to <span>TLN Ferrow Partners</span></h2>
  <div class="sec-rule" style="top:109px;left:290px;width:617px"></div>
  <p class="welcome-text abs">Lorem ipsum dolor sit amet, consectetuer adipiscing elit, sed diam nonummy nibh euismod tincidunt ut laoreet dolore magna aliquam erat volutpat. Ut wisi enim ad minim veniam, quis nostrud exerci tation ullamcorper suscipit lobortis nisl ut aliquip ex ea commodo consequat.Lorem ipsum dolor sit amet, consectetuer adipiscing elit, sed diam nonummy nibh euismod tincidunt ut laoreet dolore magna aliquam erat volutpat.</p>
  <div class="btn-outline abs">READ MORE &raquo;</div>
</section>

<section class="what-we-do">
  <h2 class="sec-title" style="top:48px">WHAT <span>WE DO</span></h2>
  <div class="sec-rule" style="top:96px"></div>
  <svg class="abs" style="left:0;top:0" width="1200" height="496" viewBox="0 0 1200 496">
    <g fill="none" stroke="#5a85b6" stroke-width="2">
      <polyline points="385,165 420,165 470,200"/>
      <polyline points="385,281 455,281"/>
      <polyline points="385,400 420,400 470,365"/>
      <polyline points="808,165 780,165 730,200"/>
      <polyline points="808,281 745,281"/>
      <polyline points="808,400 780,400 730,365"/>
    </g>
  </svg>
  <div class="hub abs"><div class="hub-inner">TLN Ferrow<br>Partners</div></div>

  <p class="wwd-item left abs" style="left:114px;top:138px">We select promising medtech startups interested in relocating to Switzerland</p>
  <p class="wwd-item left abs" style="left:114px;top:255px">We develop the relocation strategy and help implementing it</p>
  <p class="wwd-item left abs" style="left:114px;top:374px">We offer local office infrastructure</p>
  <p class="wwd-item abs" style="left:888px;top:138px">We support these startups in getting access to potential investors</p>
  <p class="wwd-item abs" style="left:888px;top:255px">We give access to a large and diverse medtech</p>
  <p class="wwd-item abs" style="left:888px;top:374px">We provide operational support and strategic expertise</p>

  <div class="wwd-icon abs" style="left:331px;top:138px"><svg width="26" height="26" viewBox="0 0 24 24"><circle cx="12" cy="7" r="4" fill="#2a2f36"/><path d="M4 22c0-6 4-8 8-8s8 2 8 8z" fill="#2a2f36"/></svg></div>
  <div class="wwd-icon abs" style="left:331px;top:254px"><svg width="26" height="26" viewBox="0 0 24 24"><circle cx="12" cy="10" r="6" fill="none" stroke="#2a2f36" stroke-width="2"/><rect x="9" y="17" width="6" height="4" fill="#2a2f36"/></svg></div>
  <div class="wwd-icon abs" style="left:331px;top:373px"><svg width="26" height="26" viewBox="0 0 24 24"><path d="M2 11L12 3l10 8M5 10v11h14V10" fill="none" stroke="#2a2f36" stroke-width="2"/><rect x="10" y="14" width="4" height="7" fill="#2a2f36"/></svg></div>
  <div class="wwd-icon abs" style="left:808px;top:138px"><svg width="26" height="26" viewBox="0 0 24 24"><path d="M2 12l5-4 5 3 5-3 5 4-8 6z" fill="#2a2f36"/></svg></div>
  <div class="wwd-icon abs" style="left:808px;top:254px"><svg width="26" height="26" viewBox="0 0 24 24"><rect x="10" y="3" width="4" height="13" rx="2" fill="#2a2f36"/><circle cx="12" cy="18" r="4" fill="#2a2f36"/></svg></div>
  <div class="wwd-icon abs" style="left:808px;top:373px"><svg width="28" height="26" viewBox="0 0 26 24"><circle cx="13" cy="7" r="3.5" fill="#2a2f36"/><circle cx="5" cy="10" r="3" fill="#2a2f36"/><circle cx="21" cy="10" r="3" fill="#2a2f36"/><path d="M7 21c0-5 3-7 6-7s6 2 6 7zM0 20c0-4 2-6 5-6s3 1 3 1zM26 20c0-4-2-6-5-6s-3 1-3 1z" fill="#2a2f36"/></svg></div>
</section>

<section class="services">
  <article class="service abs" style="left:99px">
    <div class="service-img" role="img" aria-label="Business people walking through a modern glass office lobby" style="background:linear-gradient(160deg,#c9dcef,#7fa2c8 60%,#3f5f88)">
      <div class="service-badge"><svg width="26" height="22" viewBox="0 0 26 22"><circle cx="13" cy="6" r="4" fill="#fff"/><path d="M5 20c0-5 4-7 8-7s8 2 8 7z" fill="#fff"/></svg></div>
    </div>
    <h3>Company Set-Up</h3>
    <div class="btn-pill">Read More <b>&rsaquo;</b></div>
  </article>
  <article class="service abs" style="left:443px">
    <div class="service-img" role="img" aria-label="Team members stacking hands together over a desk" style="background:linear-gradient(160deg,#b8a58e,#7d6a58 55%,#3d342c)">
      <div class="service-badge"><svg width="24" height="24" viewBox="0 0 24 24"><circle cx="12" cy="12" r="7" fill="none" stroke="#fff" stroke-width="4" stroke-dasharray="3 2.5"/><circle cx="12" cy="12" r="3" fill="#fff"/></svg></div>
    </div>
    <h3>Operational Support</h3>
    <div class="btn-pill">Read More <b>&rsaquo;</b></div>
  </article>
  <article class="service abs" style="left:786px">
    <div class="service-img" role="img" aria-label="Businessman holding a tablet with glowing technology icons" style="background:linear-gradient(160deg,#9fb5cc,#4d6784 55%,#1f2e42)">
      <div class="service-badge"><svg width="22" height="24" viewBox="0 0 22 24"><circle cx="11" cy="9" r="7" fill="none" stroke="#fff" stroke-width="2.5"/><rect x="7" y="17" width="8" height="4" fill="#fff"/></svg></div>
    </div>
    <h3>Medtech Expertise</h3>
    <div class="btn-pill">Read More <b>&rsaquo;</b></div>
  </article>
</section>

<section class="why">
  <h2 class="sec-title" style="top:42px">WHY <span>SWITZERLAND</span></h2>
  <div class="sec-rule" style="top:84px"></div>

  <p class="why-label abs" style="left:88px;top:142px">Entrepreneurial<br>Environmen</p>
  <p class="why-label abs" style="left:408px;top:142px">Investment<br>Friendliness</p>
  <p class="why-label abs" style="left:699px;top:142px;width:280px">Uncomplicated Tax System,<br>Low Tax Rates</p>
  <div class="dot-arrow abs" style="left:187px;top:202px">&rsaquo;</div>
  <div class="dot-arrow abs" style="left:507px;top:202px">&rsaquo;</div>
  <div class="dot-arrow abs" style="left:828px;top:202px">&rsaquo;</div>

  <svg class="abs" style="left:0;top:0" width="1200" height="547" viewBox="0 0 1200 547">
    <path d="M100 314 L118 314 A80 80 0 0 0 278 314 A80 80 0 0 1 438 314 A80 80 0 0 0 598 314 A80 80 0 0 1 758 314 A80 80 0 0 0 918 314 A80 80 0 0 1 1082 314 L1105 314" fill="none" stroke="#5a85b6" stroke-width="32"/>
    <g fill="#fff" stroke="#cfd8e3" stroke-width="3">
      <circle cx="198" cy="314" r="62"/><circle cx="358" cy="314" r="62"/><circle cx="518" cy="314" r="62"/>
      <circle cx="680" cy="314" r="62"/><circle cx="839" cy="314" r="62"/><circle cx="1002" cy="314" r="62"/>
    </g>
    <g fill="none" stroke="#2a2f36" stroke-width="3">
      <circle cx="198" cy="310" r="12"/><path d="M193 324h10M194 330h8M198 290v-6M180 296l-4-4M216 296l4-4M176 310h-6M220 310h6"/>
      <path d="M346 294h24M346 334h24M349 294c0 14 18 14 18 20s-18 6-18 20M367 294c0 14-18 14-18 20s18 6 18 20"/>
      <path d="M508 302c-8 8-12 18-8 26h36c4-8 0-18-8-26zM510 294h16l-4 8h-8z"/>
      <path d="M670 292c20 14 0 30 20 44M690 292c-20 14 0 30-20 44M672 304h16M672 324h16"/>
      <path d="M826 294h20l8 8v32h-28zM832 308h16M832 316h16M832 324h16"/>
      <path d="M988 296v30l-5-5M988 326l5-5M1016 332v-30l-5 5M1016 302l5 5"/>
    </g>
    <text x="518" y="320" font-family="Lato,Arial,sans-serif" font-size="14" font-weight="900" fill="#fff" text-anchor="middle">$</text>
    <text x="1002" y="320" font-family="Lato,Arial,sans-serif" font-size="16" font-weight="700" fill="#2a2f36" text-anchor="middle">$</text>
  </svg>

  <p class="why-label abs" style="left:248px;top:404px">Specialized<br>Workforce</p>
  <p class="why-label abs" style="left:570px;top:404px">Large Medtech<br>&amp; Life Sciences</p>
  <p class="why-label abs" style="left:892px;top:404px">Varied<br>Investors</p>
  <div class="dot-arrow abs" style="left:347px;top:458px">&rsaquo;</div>
  <div class="dot-arrow abs" style="left:669px;top:458px">&rsaquo;</div>
  <div class="dot-arrow abs" style="left:991px;top:458px">&rsaquo;</div>
</section>

<section class="team">
  <h2 class="sec-title" style="top:48px">OUR TEAM</h2>
  <div class="sec-rule" style="top:95px;background:rgba(255,255,255,.45)"></div>
  <p class="team-intro abs">TLN Ferrow Partners is formed by a group of individuals with many years of operational and management experience in the medtech industry, including all ares or the value chain</p>

  <div class="slide-arrow abs" style="left:72px;top:341px">&lsaquo;</div>
  <div class="slide-arrow abs" style="left:1096px;top:341px">&rsaquo;</div>

  <article class="member abs" style="left:99px">
    <div class="member-photo" role="img" aria-label="Black and white portrait of team member Marcel Dufour"></div>
    <h4>MARCEL DUFOUR</h4>
    <p>Marcel Dufour is a consultant for strategy development, marketing and sales with companies in the Medtechsector...</p>
    <div class="member-plus">+</div>
  </article>
  <article class="member abs" style="left:358px">
    <div class="member-photo" role="img" aria-label="Black and white portrait of team member Sophie Renard"></div>
    <h4>SOPHIE RENARD</h4>
    <p>Sophie Renard has a 25 years of business experience in multiple international companies, in medical Device class...</p>
    <div class="member-plus">+</div>
  </article>
  <article class="member abs" style="left:619px">
    <div class="member-photo" role="img" aria-label="Black and white portrait of team member Anton K. Weber"></div>
    <h4>ANTON K. WEBER</h4>
    <p>Anton Weber has over 25 years of business experience in the international environment as a member of the senior...</p>
    <div class="member-plus">+</div>
  </article>
  <article class="member abs" style="left:878px">
    <div class="member-photo" role="img" aria-label="Black and white portrait of team member Lena Brunner"></div>
    <h4>LENA BRUNNER</h4>
    <p>Lena Brunner is co-founder of a boutique consulting company with focus on the life science industry. Furthermore...</p>
    <div class="member-plus">+</div>
  </article>
</section>

<section class="subs">
  <h2 class="sec-title" style="top:52px">OUR <span>SUBSIDIARIES</span></h2>
  <div class="sec-rule" style="top:106px"></div>
  <div class="thin-arrow abs" style="left:62px;transform:rotate(-45deg)"></div>
  <div class="thin-arrow abs" style="left:1120px;transform:rotate(135deg)"></div>
  <div class="sub-logo abs" style="left:97px"><i></i>Veritas</div>
  <div class="sub-logo abs" style="left:268px"><i></i>Holmberg</div>
  <div class="sub-logo abs" style="left:440px"><i></i>Caldora</div>
  <div class="sub-logo abs" style="left:612px">Quanta Labs</div>
  <div class="sub-logo abs" style="left:784px"><i></i>Veritas</div>
  <div class="sub-logo abs" style="left:954px">Nordwell</div>
</section>

<footer class="site-footer">
  <div class="abs" style="left:99px;top:38px">
    <h5 class="foot-title">Quick <span>Links</span></h5>
    <ul class="quick-links" style="margin-top:14px;padding-left:10px">
      <li>Home</li><li>Services</li><li>Who We Adress</li><li>Offering</li><li>Customers</li><li>Team</li><li>Contact Us</li>
    </ul>
  </div>
  <div class="abs" style="left:324px;top:38px;width:260px">
    <h5 class="foot-title">Contact <span>Details</span></h5>
    <p class="contact-list" style="margin-top:20px">TLN Ferrow Partners SA<br>Rue des Tilleuls 14<br>2000 Lorvex<br>Switzerland</p>
    <div class="contact-line" style="margin-top:16px"><i></i>+123 456 7890</div>
    <div class="contact-line"><i></i>+123 456 7890</div>
    <div class="contact-line"><i></i>info@tlnferrow.com</div>
  </div>
  <div class="abs" style="left:639px;top:38px">
    <h5 class="foot-title">Quick <span>Contact</span></h5>
    <div style="margin-top:16px">
      <div class="field">Name</div>
      <div class="field">Email</div>
      <div class="field">Message</div>
      <div class="btn-submit">Submit</div>
    </div>
  </div>
  <div class="abs" style="left:990px;top:38px">
    <h5 class="foot-title">Follow <span>Us</span></h5>
    <div style="margin-top:20px">
      <div class="social"><i></i>Friendly</div>
      <div class="social"><i></i>Chirper</div>
      <div class="social"><i></i>Linkwork</div>
    </div>
  </div>
</footer>

<div class="copyright">Copyright &copy; 2016 TLN FERROW PARTNERS. All Rights Reserved.</div>

</body>
</html>
```